Aerospace Center needs app design

We need a design that would be a creative and innovative look of a simple idea connecting air traffic control situations with sonification.
We would like to see designs that use the elements shown in the short video which are different pads, showing 4 different colors, connecting with a degree and feeling of urgency. The different pads will be movable over screen, similar as to a whiteboard where you can move things around. Each of those pads has 4 different elements that are shown:
- ATC Event (you can chose different setups)
- Select a status (you can chose between Information, Caution and Alert. Color needs to feel more alert from Information to Alert.
- Notes box (you can open the box and write additional text on it)
- Music (you can chose different files. on the right side you can see a small group of notes. When you hover over the notes, music will be played without pressing a play or stop button.
The second video is an overview of music archival program that is connected with the pads.
Look and feel
Each slider illustrates characteristics of the customer's brand and the style your logo design should communicate.

```html
<!DOCTYPE html>
<html lang="en">
<head>
<meta charset="utf-8">
<title>AVORA – Sound Pads</title>
<link href="https://fonts.googleapis.com/css2?family=Roboto:wght@400;500;700&display=swap" rel="stylesheet">
<style>
  :root{
    --bg:#1b2140;
    --header:#1c2242;
    --sidebar:#1e2547;
    --profile:#2f3a68;
    --pad-idle:#2d3665;
    --white:#ffffff;
    --ink:#1b1f33;
    --info-a:#63cc00; --info-b:#92ea20;
    --caution-a:#e6cc00; --caution-b:#fbee22;
    --alert-a:#ee3410; --alert-b:#ff5a22;
    --badge:#ff5a3c;
    --muted:#c9cde0;
  }
  *{box-sizing:border-box;margin:0;padding:0}
  html,body{width:1200px;height:938px;overflow:hidden}
  body{background:var(--bg);font-family:'Roboto',sans-serif;color:var(--white);position:relative}

  .topbar{position:absolute;left:0;top:0;width:1200px;height:59px;background:var(--header)}
  .search{position:absolute;left:10px;top:11px;width:237px;height:37px;border:1px solid #5a6290;border-radius:19px;display:flex;align-items:center;padding:0 12px 0 18px;font-size:14px;justify-content:space-between}
  .brand{position:absolute;left:548px;top:12px;display:flex;align-items:center;gap:7px;font-size:30px;font-weight:700;letter-spacing:1px;line-height:34px}
  .brand-mark{width:16px;height:16px;background:var(--white)}
  .bell{position:absolute;left:975px;top:16px}
  .bell .count{position:absolute;left:10px;top:-2px;width:12px;height:12px;border-radius:50%;background:var(--badge);font-size:9px;text-align:center;line-height:12px}
  .divider{position:absolute;left:1017px;top:0;width:1px;height:59px;background:#2d3560}
  .user{position:absolute;left:1034px;top:8px;display:flex;align-items:center;gap:10px;font-size:16px;font-weight:500}
  .avatar{border-radius:50%;background:radial-gradient(circle at 50% 40%,#c9a58a,#5b4a44 70%);border:2px solid #e6e6ee}
  .user .avatar{width:42px;height:42px}

  .sidebar{position:absolute;left:0;top:59px;width:211px;height:879px;background:var(--sidebar)}
  .profile{position:absolute;left:0;top:6px;width:211px;height:119px;background:var(--profile);text-align:center}
  .profile .avatar{position:absolute;left:79px;top:15px;width:52px;height:52px}
  .profile .name{position:absolute;left:0;right:0;top:73px;font-size:16px;font-weight:500}
  .profile .role{position:absolute;left:0;right:0;top:97px;font-size:10px;color:var(--muted)}
  .nav{position:absolute;left:31px;top:0;list-style:none;font-size:14px}
  .nav li{position:absolute;white-space:nowrap;display:flex;align-items:center;gap:12px}
  .caret{width:0;height:0;border-left:4px solid transparent;border-right:4px solid transparent;border-top:5px solid var(--white)}

  .pad{position:absolute;width:472px;height:145px;border-radius:7px;overflow:hidden}
  .pad.info{background:linear-gradient(120deg,var(--info-a),var(--info-b))}
  .pad.caution{background:linear-gradient(120deg,var(--caution-a),var(--caution-b))}
  .pad.alert{background:linear-gradient(120deg,var(--alert-a),var(--alert-b))}
  .pad.idle{background:linear-gradient(120deg,#2a3360,#323c6c)}
  .pad-title{position:absolute;left:17px;top:13px;font-size:14px}
  .pad-close{position:absolute;left:439px;top:7px;width:27px;height:20px;background:var(--white);display:flex;align-items:center;justify-content:center}
  .field{position:absolute;width:189px;height:34px;background:var(--white);color:var(--ink);font-size:14px;padding-left:11px;display:flex;align-items:center}
  .field.select::after{content:"";position:absolute;right:9px;top:15px;border-left:4px solid transparent;border-right:4px solid transparent;border-top:5px solid var(--ink)}
  .f1{left:12px;top:49px}.f2{left:209px;top:49px}.f3{left:12px;top:91px}.f4{left:209px;top:91px}
  .sound{position:absolute;left:411px;top:55px;width:52px;height:52px;border-radius:50%;background:var(--ink);border:3px solid var(--white);display:flex;align-items:center;justify-content:center}

  .footer{position:absolute;left:0;width:1400px;top:894px;text-align:center;font-size:14px}
  .code{position:absolute;left:1170px;top:883px;font-size:9px}
</style>
</head>
<body>
<header class="topbar">
  <div class="search"><span>Search</span>
    <svg width="16" height="16" viewBox="0 0 16 16" fill="none" stroke="#fff" stroke-width="1.4"><circle cx="7" cy="7" r="5.5"/><path d="M11 11l4 4"/></svg>
  </div>
  <div class="brand"><span class="brand-mark"></span>AVORA</div>
  <div class="bell">
    <svg width="22" height="26" viewBox="0 0 22 26" fill="none" stroke="#fff" stroke-width="1.6"><path d="M4 19V11a7 7 0 0 1 14 0v8l2 2H2z"/><path d="M8.5 23a2.5 2.5 0 0 0 5 0"/></svg>
    <span class="count">0</span>
  </div>
  <div class="divider"></div>
  <div class="user"><div class="avatar" role="img" aria-label="User profile photo"></div>John Smith <span class="caret"></span></div>
</header>

<aside class="sidebar">
  <div class="profile">
    <div class="avatar" role="img" aria-label="User profile photo"></div>
    <div class="name">John Smith</div>
    <div class="role">Finibus orum</div>
  </div>
  <ul class="nav">
    <li style="top:155px">Sundboards <span class="caret"></span></li>
    <li style="top:201px">Edit Sundboards <span class="caret"></span></li>
    <li style="top:246px">Surveys</li>
    <li style="top:295px">Help</li>
    <li style="top:343px">My First Experiment</li>
  </ul>
</aside>

<main>
  <svg width="0" height="0" style="position:absolute">
    <defs>
      <g id="notes" fill="#fff">
        <path d="M4 2h2v11a3 3 0 1 1-2-2.8z"/>
        <path d="M6 2c2 1 4 2 4 5-1-1-2-2-4-2z"/>
        <path d="M11 8l10-3v11a3 3 0 1 1-2-2.8V8.6l-6 1.8V18a3 3 0 1 1-2-2.8z"/>
      </g>
      <path id="x" d="M1 1l10 10M11 1L1 11" stroke="#1b1f33" stroke-width="1.6"/>
    </defs>
  </svg>

  <section class="pad info" style="left:226px;top:86px">
    <div class="pad-title">SO1</div>
    <div class="pad-close"><svg width="12" height="12"><use href="#x"/></svg></div>
    <div class="field select f1">Landing</div><div class="field select f2">1. Information</div>
    <div class="field f3">Notes</div><div class="field select f4">Select sound file</div>
    <div class="sound"><svg width="24" height="22"><use href="#notes"/></svg></div>
  </section>
  <section class="pad info" style="left:711px;top:86px">
    <div class="pad-title">SO 2</div>
    <div class="pad-close"><svg width="12" height="12"><use href="#x"/></svg></div>
    <div class="field select f1">Landing</div><div class="field select f2">1. Information</div>
    <div class="field f3">Notes</div><div class="field select f4">Select sound file</div>
    <div class="sound"><svg width="24" height="22"><use href="#notes"/></svg></div>
  </section>

  <section class="pad caution" style="left:226px;top:243px">
    <div class="pad-title">SO 3</div>
    <div class="pad-close"><svg width="12" height="12"><use href="#x"/></svg></div>
    <div class="field select f1">Depature</div><div class="field select f2">2. Caution</div>
    <div class="field f3">Notes</div><div class="field select f4">Select sound file</div>
    <div class="sound"><svg width="24" height="22"><use href="#notes"/></svg></div>
  </section>
  <section class="pad alert" style="left:711px;top:243px">
    <div class="pad-title">SO 4</div>
    <div class="pad-close"><svg width="12" height="12"><use href="#x"/></svg></div>
    <div class="field select f1">Moon</div><div class="field select f2">3. Alert</div>
    <div class="field f3">Notes</div><div class="field select f4">Select sound file</div>
    <div class="sound"><svg width="24" height="22"><use href="#notes"/></svg></div>
  </section>

  <section class="pad idle" style="left:226px;top:399px">
    <div class="pad-title">SO 5</div>
    <div class="pad-close"><svg width="12" height="12"><use href="#x"/></svg></div>
    <div class="field select f1">Select atc event</div><div class="field select f2">Select status</div>
    <div class="field f3">Notes</div><div class="field select f4">Select sound file</div>
    <div class="sound"><svg width="24" height="22"><use href="#notes"/></svg></div>
  </section>
  <section class="pad idle" style="left:711px;top:399px">
    <div class="pad-title">SO 6</div>
    <div class="pad-close"><svg width="12" height="12"><use href="#x"/></svg></div>
    <div class="field select f1">Select atc event</div><div class="field select f2">Select atc event</div>
    <div class="field f3">Notes</div><div class="field select f4">Select sound file</div>
    <div class="sound"><svg width="24" height="22"><use href="#notes"/></svg></div>
  </section>

  <section class="pad idle" style="left:226px;top:556px">
    <div class="pad-title">SO 7</div>
    <div class="pad-close"><svg width="12" height="12"><use href="#x"/></svg></div>
    <div class="field select f1">Select atc event</div><div class="field select f2">Select atc event</div>
    <div class="field f3">Notes</div><div class="field select f4">Select sound file</div>
    <div class="sound"><svg width="24" height="22"><use href="#notes"/></svg></div>
  </section>
  <section class="pad idle" style="left:711px;top:556px">
    <div class="pad-title">SO 8</div>
    <div class="pad-close"><svg width="12" height="12"><use href="#x"/></svg></div>
    <div class="field select f1">Select atc event</div><div class="field select f2">Select atc event</div>
    <div class="field f3">Notes</div><div class="field select f4">Select sound file</div>
    <div class="sound"><svg width="24" height="22"><use href="#notes"/></svg></div>
  </section>

  <section class="pad idle" style="left:226px;top:712px">
    <div class="pad-title">SO 9</div>
    <div class="pad-close"><svg width="12" height="12"><use href="#x"/></svg></div>
    <div class="field select f1">Select atc event</div><div class="field select f2">Select atc event</div>
    <div class="field f3">Notes</div><div class="field select f4">Select sound file</div>
    <div class="sound"><svg width="24" height="22"><use href="#notes"/></svg></div>
  </section>
  <section class="pad idle" style="left:711px;top:712px">
    <div class="pad-title">SO 10</div>
    <div class="pad-close"><svg width="12" height="12"><use href="#x"/></svg></div>
    <div class="field select f1">Select atc event</div><div class="field select f2">Select atc event</div>
    <div class="field f3">Notes</div><div class="field select f4">Select sound file</div>
    <div class="sound"><svg width="24" height="22"><use href="#notes"/></svg></div>
  </section>
</main>

<div class="code">C39</div>
<footer class="footer">Copyright © 2021 - .All Right Reserved</footer>
</body>
</html>
```